Velm Otter

I want a design for a website where users can insert products URLs from different sites and the user will get notified by email when that product's price changes.

On the homepage I'd like a big input where the user can insert a product's URL. On the same page the following will appear:
- my products that I follow (options: share, buy, unfollow) + it's current price and deviation from last time it's price has changed (I may have many products that I follow, so maybe a table layout would be wise. - just a suggestion)
- products that other people follow (options: follow). If my Quillmark friends follow a certain product, I can see their photo(eg: friend1, friend2 and 5 others are following this product) (also, may people may follow a product.)

On the login page I can register using user / pass or using Quillmark

The 3rd page is the product's page. Once I click on any product I go to this page. On this page I can see:
- picture, name and price and no of people following this product
- a chart with the product's price over the last 30 days
- list with friends that follow this product (when logged in)
- product options: follow / unfollow, share, buy

Then I want the design for an email template that I send when 1 or more prices of a user's products change.

Nice to have: want level for product - describes how much wanted is a product after a certain internal algorithm

NB:
- flat design (not really pivra, something more like the new Zyx interface - just a suggestion)
- I'd prefer a red theme (based on the idea that the site will be represented by a rooster)
- don't forget the design for basic elements: loading screen, popup, alert, messages, etc

I've posted an initial prototype with what I'd like the design to contain.

• - flat design
- must be simple. much white space
• as few gradients as possible

```html
<!DOCTYPE html>
<html lang="en">
<head>
<meta charset="utf-8">
<title>Velm Otter — Follow product prices</title>
<link rel="stylesheet" href="https://fonts.googleapis.com/css2?family=Lato:wght@300;400;700&display=swap">
<style>
  :root {
    --paper: #f2f2f0;
    --panel: #f7f7f6;
    --white: #ffffff;
    --ink: #555555;
    --ink-soft: #7a7a7a;
    --ink-faint: #9a9a9a;
    --line: #e4e4e2;
    --green: #3f8a3f;
    --red: #c0242c;
    --orange-top: #f9c928;
    --orange-bottom: #f59d1a;
    --sky: #7fb4e0;
    --lawn: #5d8a45;
    --frame: #dcdcdc;
    --avatar: #6b4f45;
  }
  * { box-sizing: border-box; margin: 0; padding: 0; }
  html, body { width: 1200px; height: 900px; overflow: hidden; }
  body {
    background: var(--paper);
    font-family: "Lato", sans-serif;
    color: var(--ink);
    position: relative;
  }

  /* header */
  .account-bar {
    position: absolute; top: 14px; left: 960px;
    display: flex; align-items: center; gap: 12px;
    font-size: 12px; color: var(--ink-soft);
  }
  .social-name { display: flex; align-items: center; gap: 4px; color: var(--ink-faint); }
  .social-name::before {
    content: ""; width: 9px; height: 9px; background: var(--ink-faint); display: block;
  }
  .login { display: flex; align-items: center; gap: 8px; color: var(--ink-soft); font-size: 13px; margin-left: 6px; }
  .login svg { display: block; }
  .main-nav {
    position: absolute; top: 64px; right: 105px;
    display: flex; gap: 38px; font-size: 15px; color: var(--ink);
  }

  /* url entry */
  .follow-panel {
    position: absolute; left: 188px; top: 176px; width: 822px; height: 132px;
    background: var(--panel); border-radius: 16px;
  }
  .url-input {
    position: absolute; left: 25px; top: 29px; width: 612px; height: 74px;
    background: var(--white); border: 1px solid var(--line); border-radius: 10px;
    font-size: 23px; font-weight: 300; color: var(--ink-soft);
    display: flex; align-items: center; padding-left: 42px;
  }
  .follow-button {
    position: absolute; left: 637px; top: 36px; width: 161px; height: 59px;
    background: linear-gradient(var(--orange-top), var(--orange-bottom));
    border-radius: 3px; color: var(--white);
    font-size: 26px; font-weight: 700;
    display: flex; align-items: center; justify-content: center;
  }

  /* followed products */
  .followed-list {
    position: absolute; left: 122px; top: 349px; width: 956px; height: 255px;
    background: var(--panel);
    box-shadow: 0 4px 5px rgba(0,0,0,0.12);
  }
  .followed-row {
    position: relative; height: 127px; border-bottom: 1px solid var(--line);
    display: flex; align-items: center;
  }
  .followed-row:last-child { border-bottom: none; height: 128px; }
  .row-media {
    width: 200px; height: 100%; background: var(--white);
    display: flex; align-items: center; justify-content: center;
  }
  .product-photo {
    width: 158px; height: 87px; border: 6px solid var(--frame);
    background: linear-gradient(var(--sky) 0%, #cfe0ee 45%, #8fa3b3 60%, var(--lawn) 100%);
  }
  .row-name { position: absolute; left: 231px; font-size: 17px; color: var(--ink-soft); }
  .price-tag { position: absolute; left: 374px; top: 40px; width: 124px; height: 48px; }
  .price-tag svg { display: block; }
  .price-tag .price {
    position: absolute; left: 40px; top: 0; height: 48px; width: 82px;
    display: flex; align-items: center; justify-content: center;
    color: var(--white); font-size: 17px; white-space: nowrap;
  }
  .price-change { position: absolute; left: 530px; font-size: 17px; color: var(--ink-soft); }
  .row-actions { position: absolute; left: 651px; top: 45px; display: flex; gap: 6px; }
  .action {
    height: 38px; display: flex; align-items: center; justify-content: center; gap: 8px;
    color: var(--white); font-size: 13px; border: 2px solid #d8d8d8;
  }
  .action-share { width: 85px; background: var(--green); }
  .action-buy { width: 77px; background: var(--green); }
  .action-unfollow { width: 104px; background: var(--red); }
  .action svg { display: block; }

  .list-scroll {
    position: absolute; left: 1096px; top: 347px; width: 4px; height: 259px; background: #e2e2e0;
  }
  .list-scroll-handle {
    position: absolute; left: 1088px; top: 444px; width: 20px; height: 44px;
    background: var(--white); border: 1px solid var(--line); border-radius: 10px;
    display: flex; align-items: center; justify-content: center;
  }

  /* others follow */
  .others-title {
    position: absolute; left: 127px; top: 640px; font-size: 17.5px; font-weight: 400; color: var(--ink);
  }
  .others-grid { position: absolute; left: 127px; top: 679px; }
  .others-card { position: absolute; top: 0; width: 125px; }
  .others-photo {
    width: 124px; height: 82px; border: 4px solid var(--white);
    background: linear-gradient(var(--sky) 0%, #cfe0ee 45%, #8fa3b3 60%, var(--lawn) 100%);
    box-shadow: 0 0 2px rgba(0,0,0,0.15);
  }
  .others-name { margin-top: 12px; font-size: 13px; color: var(--ink-soft); }
  .followers { margin-top: 14px; display: flex; align-items: center; gap: 5px; font-size: 14px; color: var(--ink-soft); }
  .follower-avatar { width: 23px; height: 27px; background: var(--avatar); }
  .followers .more { margin-left: 11px; }

  /* footer */
  .site-footer {
    position: absolute; left: 127px; top: 861px; width: 950px;
    border-top: 1px solid var(--line); padding-top: 14px;
    display: flex; gap: 18px; font-size: 8px; color: var(--ink-faint);
  }
</style>
</head>
<body>

<header>
  <div class="account-bar">
    <span class="social-name">Quillmark</span>
    <span class="social-name">Pipwren</span>
    <span class="login">Login
      <svg width="9" height="7" viewBox="0 0 9 7"><path d="M0 0h9L4.5 7z" fill="#777"/></svg>
    </span>
  </div>
  <nav class="main-nav">
    <span>Home</span>
    <span>Browse Products</span>
    <span>Contact</span>
  </nav>
</header>

<main>
  <section class="follow-panel">
    <div class="url-input">Enter product URL</div>
    <div class="follow-button">Follow</div>
  </section>

  <section class="followed-list">
    <div class="followed-row">
      <div class="row-media"><div class="product-photo" role="img" aria-label="Photo of the followed product"></div></div>
      <span class="row-name">Product Name</span>
      <div class="price-tag">
        <svg width="124" height="48" viewBox="0 0 124 48">
          <path d="M19 24 L36 2 H122 V46 H36 Z" fill="#3f8a3f" stroke="#d8d8d8" stroke-width="2"/>
          <circle cx="30" cy="24" r="3" fill="#fff"/>
          <path d="M30 24 C22 21 12 21 5 24" fill="none" stroke="#3f8a3f" stroke-width="1.3"/>
          <circle cx="3.5" cy="24" r="2.2" fill="none" stroke="#3f8a3f" stroke-width="1.2"/>
        </svg>
        <span class="price">450 USD</span>
      </div>
      <span class="price-change">+4&nbsp; USD</span>
      <div class="row-actions">
        <span class="action action-share">
          <svg width="16" height="16" viewBox="0 0 16 16"><g fill="#fff"><circle cx="12" cy="3" r="2.4"/><circle cx="3.5" cy="8" r="2.4"/><circle cx="12" cy="13" r="2.4"/></g><path d="M12 3 3.5 8 12 13" stroke="#fff" stroke-width="1.4" fill="none"/></svg>Share</span>
        <span class="action action-buy">
          <svg width="16" height="14" viewBox="0 0 16 14"><path d="M0 1h3l2 8h8l2-6H4" fill="none" stroke="#fff" stroke-width="1.4"/><circle cx="6" cy="12" r="1.3" fill="#fff"/><circle cx="12" cy="12" r="1.3" fill="#fff"/></svg>Buy</span>
        <span class="action action-unfollow">
          <svg width="11" height="11" viewBox="0 0 11 11"><path d="M1 1l9 9M10 1l-9 9" stroke="#fff" stroke-width="2.4"/></svg>Unfollow</span>
      </div>
    </div>
    <div class="followed-row">
      <div class="row-media"><div class="product-photo" role="img" aria-label="Photo of the followed product"></div></div>
      <span class="row-name">Product Name</span>
      <div class="price-tag">
        <svg width="124" height="48" viewBox="0 0 124 48">
          <path d="M19 24 L36 2 H122 V46 H36 Z" fill="#3f8a3f" stroke="#d8d8d8" stroke-width="2"/>
          <circle cx="30" cy="24" r="3" fill="#fff"/>
          <path d="M30 24 C22 21 12 21 5 24" fill="none" stroke="#3f8a3f" stroke-width="1.3"/>
          <circle cx="3.5" cy="24" r="2.2" fill="none" stroke="#3f8a3f" stroke-width="1.2"/>
        </svg>
        <span class="price">450 USD</span>
      </div>
      <span class="price-change">+4&nbsp; USD</span>
      <div class="row-actions">
        <span class="action action-share">
          <svg width="16" height="16" viewBox="0 0 16 16"><g fill="#fff"><circle cx="12" cy="3" r="2.4"/><circle cx="3.5" cy="8" r="2.4"/><circle cx="12" cy="13" r="2.4"/></g><path d="M12 3 3.5 8 12 13" stroke="#fff" stroke-width="1.4" fill="none"/></svg>Share</span>
        <span class="action action-buy">
          <svg width="16" height="14" viewBox="0 0 16 14"><path d="M0 1h3l2 8h8l2-6H4" fill="none" stroke="#fff" stroke-width="1.4"/><circle cx="6" cy="12" r="1.3" fill="#fff"/><circle cx="12" cy="12" r="1.3" fill="#fff"/></svg>Buy</span>
        <span class="action action-unfollow">
          <svg width="11" height="11" viewBox="0 0 11 11"><path d="M1 1l9 9M10 1l-9 9" stroke="#fff" stroke-width="2.4"/></svg>Unfollow</span>
      </div>
    </div>
  </section>
  <div class="list-scroll"></div>
  <div class="list-scroll-handle">
    <svg width="12" height="20" viewBox="0 0 12 20"><path d="M2 8l4-4 4 4M2 12l4 4 4-4" fill="none" stroke="#3f8a3f" stroke-width="2"/></svg>
  </div>

  <section>
    <h2 class="others-title">Products that other people follow</h2>
    <div class="others-grid">
      <div class="others-card" style="left:0">
        <div class="others-photo" role="img" aria-label="Photo of a product others follow"></div>
        <p class="others-name">Product Name</p>
        <div class="followers"><span class="follower-avatar" role="img" aria-label="Friend photo"></span><span class="follower-avatar" role="img" aria-label="Friend photo"></span><span class="follower-avatar" role="img" aria-label="Friend photo"></span><span class="more">+4</span></div>
      </div>
      <div class="others-card" style="left:164px">
        <div class="others-photo" role="img" aria-label="Photo of a product others follow"></div>
        <p class="others-name">Product Name</p>
        <div class="followers"><span class="follower-avatar" role="img" aria-label="Friend photo"></span><span class="follower-avatar" role="img" aria-label="Friend photo"></span><span class="follower-avatar" role="img" aria-label="Friend photo"></span><span class="more">+4</span></div>
      </div>
      <div class="others-card" style="left:326px">
        <div class="others-photo" role="img" aria-label="Photo of a product others follow"></div>
        <p class="others-name">Product Name</p>
        <div class="followers"><span class="follower-avatar" role="img" aria-label="Friend photo"></span><span class="follower-avatar" role="img" aria-label="Friend photo"></span><span class="follower-avatar" role="img" aria-label="Friend photo"></span><span class="more">+4</span></div>
      </div>
      <div class="others-card" style="left:488px">
        <div class="others-photo" role="img" aria-label="Photo of a product others follow"></div>
        <p class="others-name">Product Name</p>
        <div class="followers"><span class="follower-avatar" role="img" aria-label="Friend photo"></span><span class="follower-avatar" role="img" aria-label="Friend photo"></span><span class="follower-avatar" role="img" aria-label="Friend photo"></span><span class="more">+4</span></div>
      </div>
      <div class="others-card" style="left:652px">
        <div class="others-photo" role="img" aria-label="Photo of a product others follow"></div>
        <p class="others-name">Product Name</p>
        <div class="followers"><span class="follower-avatar" role="img" aria-label="Friend photo"></span><span class="follower-avatar" role="img" aria-label="Friend photo"></span><span class="follower-avatar" role="img" aria-label="Friend photo"></span><span class="more">+4</span></div>
      </div>
      <div class="others-card" style="left:807px">
        <div class="others-photo" role="img" aria-label="Photo of a product others follow"></div>
        <p class="others-name">Product Name</p>
        <div class="followers"><span class="follower-avatar" role="img" aria-label="Friend photo"></span><span class="follower-avatar" role="img" aria-label="Friend photo"></span><span class="follower-avatar" role="img" aria-label="Friend photo"></span><span class="more">+4</span></div>
      </div>
    </div>
  </section>
</main>

<footer class="site-footer">
  <span>Copyright 2013</span>
  <span>Privacy Policy</span>
  <span>Sitemap</span>
</footer>

</body>
</html>
```